banner for website

I need a new banner for my website. My website now is. www.brightmeadowkitchen.net, but I'm changing it to Fresh Rooted Days and I need a new banner. I want me to be who it's about. I am my brand. I'm Marla Prewitt. So, my name needs to be prominent in the banner along with my photo, which I'm attaching. I want my photo very prominent in the banner and very large. I am attaching my two favorites.
I need the banner plain ( with out the newsletter sign up optin part), so I can use it on my newsletters, emails and letter head, as well. I would like it to be inviting. I I have a certain color scheme I use. Deep dark brown letters with blues and greens. Very earthy and psychologically grounded. I would like to keep that color scheme. In my website banner, I need a opt in to sign up for my free monthly newsletter and receive my Free Pantry Starter Booklet.

I want the shopping guide to be small and pleasant looking and to say: "Sign up to receive your Free Pantry Starter Booklet and monthly newsletter."

I only want my banner to say: "Fresh Rooted Days" "Marla Prewitt"

I would also like to have part of the banner without the sign in for the newsletter part off of it. And also one with only the "Fresh Rooted Days" and one with "Fresh Rooted Days" and "Marla Prewitt" without the newsletter sign up part on it either.

I hope you can do this for me. I look forward to seeing your design! Sincerely, Marla
Updates

Project Deadline Extended Reason: I couldn't view the designs so I couldn't look at the ones submitted. I just now got into the website with your company's help. I don't want to be penalized because of a problem with the log in at your site. That was not my fault. Please let me know your thoughts. Added Monday, May 9, 2016

Target Market(s)

people over 40 who have bad health or who want to learn how to be a vegetarian for better health.

Number of Pages Required

1 page

Requirements
Must have
• I want the shopping guide to be small and pleasant looking and to say: "Sign up to receive your Free Pantry Starter Booklet and monthly newsletter." I would like it to blend and be elegant and not in the middle of the banner or across my face.
• I only want my banner to say: "Fresh Rooted Days" "Marla Prewitt"
• I would also like to have part of the banner without the sign in for the newsletter part off of it. And also one with only the "Fresh Rooted Days" and one with "Fresh Rooted Days" and "Marla Prewitt" without the newsletter sign up part on it either.
Nice to have
• Nice font and colors. I want the background to be plants and earthy and inviting.
Should not have
• I updated and added two new photos. I think the one you were using with me in the red top looked funny under my eyes. it was too pink or something. I uploaded a better version of that photo. in hopes that it looks better. Please switch those out if you are using the one with me in the red top.

```html
<!DOCTYPE html>
<html lang="en">
<head>
<meta charset="utf-8">
<title>Fresh Rooted Days – Website Banners</title>
<link rel="stylesheet" href="https://fonts.googleapis.com/css2?family=Josefin+Sans:wght@700&family=Marck+Script&family=Fjalla+One&display=swap">
<style>
  :root {
    --canvas: #9a9a9a;
    --navy: #2a3242;
    --navy-mid: #3a4454;
    --slate: #8b96a2;
    --white: #ffffff;
    --photo-warm: #b8896c;
    --photo-red: #8e2a24;
    --photo-green: #4f6b34;
  }
  * { margin: 0; padding: 0; box-sizing: border-box; }
  html, body {
    width: 1200px;
    height: 948px;
    overflow: hidden;
    background: var(--canvas);
  }
  .canvas {
    position: relative;
    width: 1200px;
    height: 948px;
  }
  .banner {
    position: absolute;
    left: 0;
    width: 1200px;
    overflow: hidden;
    background: linear-gradient(90deg, var(--navy) 0%, var(--navy) 62%, var(--navy-mid) 80%, var(--slate) 100%);
  }
  .banner--plain { top: 0; height: 333px; }
  .banner--signup { top: 625px; height: 289px; }

  .portrait {
    position: absolute;
    left: 0;
    top: 0;
    height: 100%;
    background:
      radial-gradient(ellipse 35% 22% at 45% 22%, #e6c9a8 0%, rgba(230,201,168,0) 100%),
      radial-gradient(ellipse 60% 30% at 40% 60%, var(--photo-red) 0%, rgba(142,42,36,0) 100%),
      radial-gradient(ellipse 70% 35% at 55% 88%, var(--photo-green) 0%, rgba(79,107,52,0) 100%),
      linear-gradient(180deg, var(--navy) 0%, var(--photo-warm) 45%, var(--photo-green) 100%);
  }
  .banner--plain .portrait { width: 275px; }
  .banner--signup .portrait { width: 240px; }

  .brand-dot {
    position: absolute;
    border-radius: 50%;
    background: var(--white);
  }
  .banner--plain .brand-dot { left: 312px; top: 128px; width: 72px; height: 72px; }
  .banner--signup .brand-dot { left: 256px; top: 155px; width: 52px; height: 52px; }

  .brand-name {
    position: absolute;
    font-family: "Josefin Sans", sans-serif;
    font-weight: 700;
    font-variant: small-caps;
    color: var(--white);
    white-space: nowrap;
    letter-spacing: 1px;
  }
  .banner--plain .brand-name { left: 440px; top: 132px; font-size: 62px; }
  .banner--signup .brand-name { left: 318px; top: 160px; font-size: 44px; }

  .person-name {
    position: absolute;
    font-family: "Marck Script", cursive;
    color: var(--white);
    white-space: nowrap;
  }
  .banner--plain .person-name { left: 725px; top: 198px; font-size: 60px; }
  .banner--signup .person-name { left: 505px; top: 210px; font-size: 46px; }

  .signup {
    position: absolute;
    right: 30px;
    top: 14px;
    width: 420px;
    font-family: "Fjalla One", sans-serif;
    font-size: 26px;
    line-height: 36px;
    color: var(--white);
    text-align: center;
    letter-spacing: 1px;
  }
  .signup__name { font-family: "Marck Script", cursive; font-size: 28px; }
</style>
</head>
<body>
<main class="canvas">
  <section class="banner banner--plain">
    <div class="portrait" role="img" aria-label="Portrait photo of Marla Prewitt smiling, holding a basket of fresh garden greens and herbs"></div>
    <span class="brand-dot"></span>
    <h1 class="brand-name">Fresh Rooted Days</h1>
    <p class="person-name">Marla Prewitt</p>
  </section>

  <section class="banner banner--signup">
    <div class="portrait" role="img" aria-label="Portrait photo of Marla Prewitt smiling, holding a basket of fresh garden greens and herbs"></div>
    <span class="brand-dot"></span>
    <h2 class="brand-name">Fresh Rooted Days</h2>
    <p class="person-name">Marla Prewitt</p>
    <p class="signup">Sign up to receive <span class="signup__name">Marla's</span><br>Free Pantry Starter Booklet<br>and monthly newsletter</p>
  </section>
</main>
</body>
</html>
```